ORVET - Helping People with Disabilities

ORVET is a nonprofit that strives to enable people with physical disabilities to live meaningful, quality lives. ORVET needs a professional attractive website that:
• establishes a strong brand image
• presents Orvet's services to those who need it
• raises funds from potential donors
Please see WORD DOC attached for more information about design vision.

Target Market(s)

people with disabilities

Industry/Entity Type

charity website

Number of Pages Required

2 page

Font styles to use
Sans Serif

Requirements
Must have
• 1. 2 pages means 1 design for homepage and 1 design for top of inner pages (banner ideas)
Nice to have
• please see attached design brief (WORD DOC)

```html
<!DOCTYPE html>
<html lang="en">
<head>
<meta charset="utf-8">
<title>ORVET – Helping People with Disabilities</title>
<link rel="stylesheet" href="https://fonts.googleapis.com/css2?family=Inter:wght@300;400;500;600&display=swap">
<style>
:root{
  --amber:#eda733;
  --teal:#006a69;
  --aqua:#27bdbe;
  --mist:#dbe7e8;
  --page:#f4f6f7;
  --canvas:#eeeff0;
  --ink:#4a5656;
  --muted:#7d8787;
  --white:#ffffff;
}
*{box-sizing:border-box;margin:0;padding:0}
html,body{width:1200px;height:2993px;overflow:hidden}
body{background:var(--canvas);font-family:"Inter",Arial,sans-serif;color:var(--ink);position:relative}
.abs{position:absolute}

/* style panel */
.guide-brand{left:203px;top:135px;font-size:24px;font-weight:600;color:var(--teal);display:flex;align-items:center;gap:8px}
.guide-brand i{width:18px;height:18px;background:var(--teal);display:block}
.guide-title{font-size:26px;font-weight:400;color:#222}
.guide-font{left:517px;top:147px;font-size:16px;font-weight:300;color:var(--muted)}
.swatch{top:138px;width:42px;height:42px;border-radius:50%}
.swatch-label{top:188px;width:52px;text-align:center;font-size:9px;color:#555}

.site{position:absolute;left:220px;top:279px;width:794px;height:2614px;background:var(--page);overflow:hidden}
.btn{position:absolute;background:var(--amber);color:var(--white);font-size:8px;font-weight:600;display:flex;align-items:center;justify-content:center;gap:6px}
.btn svg{width:9px;height:9px}
.link{font-size:7.5px;color:var(--aqua);border-bottom:1px solid var(--amber);padding-bottom:2px;display:inline-block}
h2{font-weight:500;color:var(--teal);font-size:25px;letter-spacing:-.2px}

/* top bar + nav */
.topbar{left:309px;top:0;width:378px;height:19px;background:var(--mist);font-size:6.5px;color:var(--teal);display:flex;align-items:center;padding:0 45px}
.topbar .follow{display:flex;align-items:center;gap:4px}
.topbar .dot{width:5px;height:5px;border-radius:50%;background:var(--aqua)}
.topbar .actions{margin-left:auto;display:flex;gap:12px}
.brand{left:106px;top:28px;font-size:15px;font-weight:600;color:var(--teal);display:flex;align-items:center;gap:5px}
.brand i{width:9px;height:9px;background:var(--teal);display:block}
.nav{top:37px;font-size:7.5px;color:var(--aqua)}

/* hero */
.hero-teal{left:6px;top:66px;width:248px;height:372px;background:var(--teal)}
.hero-photo{left:254px;top:66px;width:533px;height:372px;background:linear-gradient(120deg,#3a3d44 0%,#8a6a3c 35%,#d49b2c 55%,#2b9c94 75%,#5b5f66 100%)}
.hero-card{left:106px;top:149px;width:297px;height:208px;background:var(--white)}
.hero-card h1{position:absolute;left:58px;top:34px;font-size:30px;line-height:29px;font-weight:400;color:var(--teal);letter-spacing:-.3px}
.hero-card h1 b{font-weight:500}
.caption{left:6px;top:438px;width:781px;height:30px;background:var(--mist);font-size:7px;color:var(--teal);display:flex;align-items:center;justify-content:center}
.caption .arr{position:absolute;color:var(--aqua);font-size:10px}

/* about */
.about-text{left:106px;top:572px;width:275px;font-size:8.5px;line-height:12.6px;color:var(--ink)}
.about-text p{margin-bottom:10px}

/* offers */
.card{top:842px;width:189px;height:201px;background:var(--white)}
.card .ph{height:91px}
.card h3{font-size:11.5px;font-weight:500;color:var(--teal);margin:14px 0 0 14px}
.card p{font-size:7.5px;line-height:11.5px;margin:8px 14px 0 14px;color:var(--ink)}
.card .link{position:absolute;left:14px;top:171px}

/* banner */
.banner{left:6px;top:1098px;width:781px;height:387px;background:linear-gradient(100deg,#4a3b3e 0%,#c9c7cb 30%,#e9e6e3 50%,#8c6d62 70%,#d5d8dc 100%)}
.banner-box{left:106px;top:1312px;width:581px;height:173px;background:var(--teal);text-align:center;color:var(--white)}
.banner-box p{font-size:22px;font-weight:300;line-height:25px;margin-top:37px}
.banner-box p b{font-weight:600}

/* news */
.news{left:106px;width:340px;height:77px}
.news .ph{position:absolute;left:0;top:0;width:119px;height:77px}
.news .date{position:absolute;left:132px;top:0;font-size:6px;color:#8a9a9a}
.news h4{position:absolute;left:132px;top:10px;font-size:11px;font-weight:500;color:var(--teal)}
.news p{position:absolute;left:132px;top:29px;width:200px;font-size:7.2px;line-height:11.5px}
.news .link{position:absolute;left:132px;top:64px}
.map{left:560px;top:1592px;width:94px;height:261px;background:linear-gradient(180deg,#dbe7e8,#cfdfe0);border-radius:40px 40px 50% 50%}

/* contact */
.contact{left:6px;top:1902px;width:781px;height:418px;background:linear-gradient(90deg,#7a6243 0%,#a3845c 30%,#c58a6a 55%,#1f7a52 75%,#b37a8a 100%)}
.form{left:106px;top:1958px;width:297px;height:339px;background:var(--white)}
.form h2{position:absolute;left:20px;top:22px}
.form label{position:absolute;font-size:6.5px;color:var(--ink)}
.form .field{position:absolute;background:var(--mist)}

/* footer */
.foot h5{font-size:9px;font-weight:500;color:var(--teal)}
.foot .t{font-size:7.5px;line-height:12px;color:var(--aqua)}
.circle{width:19px;height:19px;border:1px solid var(--aqua);border-radius:50%;display:inline-block;margin-right:3px}
.rule{left:106px;top:2532px;width:581px;height:1px;background:var(--teal)}
.bottom{top:2552px;font-size:7px;color:var(--teal)}
</style>
</head>
<body>

<!-- style panel -->
<div class="abs guide-brand"><i></i>ORVET</div>
<div class="abs guide-title" style="left:517px;top:102px">Fonts:</div>
<div class="abs guide-font">Alpine Grotesk</div>
<div class="abs guide-title" style="left:840px;top:102px">Colors:</div>
<div class="abs swatch" style="left:842px;background:var(--amber)"></div>
<div class="abs swatch" style="left:894px;background:var(--teal)"></div>
<div class="abs swatch" style="left:946px;background:var(--aqua)"></div>
<div class="abs swatch" style="left:997px;background:var(--mist)"></div>
<div class="abs swatch-label" style="left:837px">#eda733</div>
<div class="abs swatch-label" style="left:889px">#006a69</div>
<div class="abs swatch-label" style="left:941px">#27bdbe</div>
<div class="abs swatch-label" style="left:992px">#dbe7e8</div>

<div class="site">

  <!-- header -->
  <div class="abs topbar">
    <div class="follow">Follow Us: <span class="dot"></span><span class="dot"></span><span class="dot"></span></div>
    <div class="actions"><span>Join ORVET</span><span>Donate for Them</span></div>
  </div>
  <div class="abs brand"><i></i>ORVET</div>
  <span class="abs nav" style="left:308px">About</span>
  <span class="abs nav" style="left:354px">Programs</span>
  <span class="abs nav" style="left:412px">Rehabilitation and Sports</span>
  <span class="abs nav" style="left:520px">Rights Realization</span>
  <span class="abs nav" style="left:605px">News</span>
  <span class="abs nav" style="left:651px">Contact Us</span>

  <!-- hero -->
  <div class="abs hero-teal"></div>
  <div class="abs hero-photo" role="img" aria-label="Smiling young woman in a yellow sweater holding an ORVET folder, with friends behind her"></div>
  <div class="abs hero-card">
    <h1>A Good Life<br>for Everyone,<br><b>Like Everyone</b></h1>
    <div class="btn" style="left:58px;top:140px;width:137px;height:29px">
      <svg viewBox="0 0 10 10"><path d="M5 9 1 5a2.2 2.2 0 0 1 4-3 2.2 2.2 0 0 1 4 3Z" fill="#fff"/></svg>Donate to Help Them Now</div>
  </div>
  <div class="abs caption">
    <span class="arr" style="left:100px">‹</span>
    Maple House, a day care center for people with physical disabilities, recently put smiles on the faces of children in the south who lived near
    <span class="arr" style="left:676px">›</span>
  </div>

  <!-- about -->
  <h2 class="abs" style="left:106px;top:518px">About Orvet Association</h2>
  <div class="abs about-text">
    <p>The Orvet Association strives to enable people with physical disabilities to live meaningful and high-quality lives.</p>
    <p>Since 1952, spurred by the polio virus outbreak, ORVET been providing a wide range of activities for children and adults with disabilities to enable them to live independently and integrate into society.</p>
    <p>In over 30 cities across the country, we provide a wide variety of programs for children and adults with physical disabilities and their family members, helping to improve motor skills, build self-confidence, and create a sense of long-term ability.</p>
  </div>
  <span class="abs link" style="left:106px;top:723px">More About Us</span>
  <svg class="abs" style="left:451px;top:523px" width="237" height="210" viewBox="0 0 237 210" role="img" aria-label="Group photo of members in front of a day center, framed in a triangle">
    <defs><linearGradient id="tri" x1="0" y1="0" x2="0" y2="1"><stop offset="0" stop-color="#c9d6dc"/><stop offset="1" stop-color="#6f8a86"/></linearGradient></defs>
    <polygon points="118,0 237,210 0,210" fill="url(#tri)"/>
    <polygon points="118,0 237,210 0,210" fill="none" stroke="#27bdbe" stroke-width="3"/>
  </svg>

  <!-- offers -->
  <h2 class="abs" style="left:0;width:794px;text-align:center;top:794px">What We Offer You</h2>
  <div class="abs card" style="left:6px"><div class="ph" role="img" aria-label="Large group of members posing outdoors" style="background:linear-gradient(135deg,#6f8e5a,#b8bcc0)"></div>
    <h3>Education</h3><p>ORVET works to impart education and knowledge to people with disabilities and operates the dedicated campus ...</p><span class="link">Find Out More</span></div>
  <div class="abs card" style="left:203px"><div class="ph" role="img" aria-label="Wheelchair football player on a gym court" style="background:linear-gradient(135deg,#d9a24a,#6fa07a)"></div>
    <h3>Sports and Rehab</h3><p>ORVET encourages people with disabilities to play sports and find new strengths in themselves...</p><span class="link">Find Out More</span></div>
  <div class="abs card" style="left:400px"><div class="ph" role="img" aria-label="People talking together at an event" style="background:linear-gradient(135deg,#3b3535,#a88a7c)"></div>
    <h3>Right Realization</h3><p>ORVET promotes policies concerning people with physical-motor disabilities, promotes their rights, ...</p><span class="link">Find Out More</span></div>
  <div class="abs card" style="left:597px"><div class="ph" role="img" aria-label="Bright empty room in an accessible house" style="background:linear-gradient(135deg,#e4e8ea,#9aa6ae)"></div>
    <h3>Community Infrastructure</h3><p>ORVET owns the association's houses all over the country,rehabilitation day centers,...</p><span class="link">Find Out More</span></div>

  <!-- banner -->
  <div class="abs banner" role="img" aria-label="Group of volunteers and members raising their hands in celebration"></div>
  <div class="abs banner-box">
    <p>Even people with disabilities can be<br><b>with everyone, like everyone</b></p>
    <div class="btn" style="left:222px;top:102px;width:137px;height:31px">
      <svg viewBox="0 0 10 10"><path d="M5 9 1 5a2.2 2.2 0 0 1 4-3 2.2 2.2 0 0 1 4 3Z" fill="#fff"/></svg>Don't Leave Them Behind</div>
  </div>

  <!-- news + branches -->
  <h2 class="abs" style="left:106px;top:1534px">Recent News</h2>
  <h2 class="abs" style="right:107px;top:1534px">Our Branches</h2>
  <div class="abs news" style="top:1586px"><div class="ph" role="img" aria-label="Members hiking outdoors" style="background:linear-gradient(135deg,#b6a98a,#6f8a6a)"></div>
    <span class="date">9/23/2023</span><h4>Blog Title 1 Goes Here</h4><p>Lorem Ipsum has been the industry's standard dummy text ever since the 1500s, when an unknown</p><span class="link">Read Full Article</span></div>
  <div class="abs news" style="top:1678px"><div class="ph" role="img" aria-label="Musicians performing on stage" style="background:linear-gradient(135deg,#2d2a2a,#8a6a4a)"></div>
    <span class="date">9/23/2023</span><h4>Blog Title 2 Goes Here</h4><p>Lorem Ipsum has been the industry's standard dummy text ever since the 1500s, when an unknown</p><span class="link">Read Full Article</span></div>
  <div class="abs news" style="top:1770px"><div class="ph" role="img" aria-label="Audience watching a presentation" style="background:linear-gradient(135deg,#5a6a5a,#3a3636)"></div>
    <span class="date">9/23/2023</span><h4>Blog Title 3 Goes Here</h4><p>Lorem Ipsum has been the industry's standard dummy text ever since the 1500s, when an unknown</p><span class="link">Read Full Article</span></div>
  <div class="abs map" role="img" aria-label="Country map showing branch locations"></div>

  <!-- contact -->
  <div class="abs contact" role="img" aria-label="Two smiling women in an art room, one seated in a wheelchair"></div>
  <div class="abs form">
    <h2>Contact Us</h2>
    <label style="left:20px;top:64px">Name*</label>
    <label style="left:153px;top:64px">Phone*</label>
    <div class="field" style="left:20px;top:76px;width:124px;height:23px"></div>
    <div class="field" style="left:153px;top:76px;width:124px;height:23px"></div>
    <label style="left:20px;top:112px">Email Adress*</label>
    <div class="field" style="left:20px;top:124px;width:257px;height:23px"></div>
    <label style="left:20px;top:160px">Message*</label>
    <div class="field" style="left:20px;top:172px;width:257px;height:64px"></div>
    <div class="btn" style="left:20px;top:254px;width:117px;height:30px">
      <svg viewBox="0 0 10 10"><rect x="1" y="2" width="8" height="6" fill="#fff"/><path d="M1 2 5 5.5 9 2" stroke="#eda733" fill="none"/></svg>Send Your Message</div>
  </div>

  <!-- footer -->
  <div class="abs foot" style="left:106px;top:2368px;width:150px">
    <h5>About Us</h5>
    <p class="t" style="margin-top:13px">The Orvet Association strives to enable people with physical disabilities to live meaningful and high-quality lives.</p>
  </div>
  <div class="abs foot" style="left:371px;top:2368px">
    <h5>Follow Us</h5>
    <div style="margin-top:12px"><span class="circle"></span><span class="circle"></span><span class="circle"></span></div>
  </div>
  <div class="abs foot" style="left:546px;top:2368px">
    <h5>About Us</h5>
    <p class="t" style="margin-top:9px">info@orvet-example.org</p>
    <p class="t" style="margin-top:4px">03-5550141</p>
    <p class="t" style="margin-top:4px">03-5550828</p>
    <p class="t" style="margin-top:4px;line-height:11px">12 Cedar Street<br>PO Box 4410<br>Harbor City 4400120</p>
  </div>
  <div class="btn" style="left:546px;top:2484px;width:141px;height:28px">
    <svg viewBox="0 0 10 10"><path d="M2 1h2l1 2-1.2 1a6 6 0 0 0 2.2 2.2L7 5l2 1v2c-4 .5-8-3.5-7-7Z" fill="#fff"/></svg>Speak to Fundraising Center</div>
  <div class="abs rule"></div>
  <span class="abs bottom" style="left:106px;font-weight:600">ORVET</span>
  <span class="abs bottom" style="left:0;width:794px;text-align:center">© 2023 Orvet</span>
  <span class="abs bottom" style="right:107px">↑ Scroll to Top</span>

</div>
</body>
</html>
```